Business card - mobile service

O KiraTel is a mobile family safety service based on tablets and smartphones.
The business card must have:
BASIC INFO
Company Logo
Name
Position / Job Title: Co-founder
Mobile Phone Number: +55 (11) 5080 6172
Land Line: +55 (11) 9087 614352
Email Address: name@kiratel-example.com
Web Site URL: www.kiratel-example.com
PROMOTIONAL INFO
Try KiraTel free Today!
Your personal promo code: xxxx-2222-uuuu-7777-1234
Promo code text explanation with the instructions about the trial offer
Updates
Dears,
One more must have: the KiraTel slogan:
Industry/Entity Type
Safety
Look and feel
Each slider illustrates characteristics of the customer's brand and the style your logo design should communicate.

```html
<!DOCTYPE html>
<html lang="en">
<head>
<meta charset="utf-8">
<title>KiraTel business card</title>
<link href="https://fonts.googleapis.com/css2?family=Open+Sans:wght@300;400;600;700&display=swap" rel="stylesheet">
<style>
  :root {
    --blue: #1aa7e1;
    --blue-deep: #0d96d6;
    --yellow: #fbb80f;
    --ink: #222222;
    --card: #ffffff;
    --bg-top: #dcdcdc;
    --bg-bottom: #f3f3f3;
  }
  html, body { margin: 0; padding: 0; overflow: hidden; }
  .canvas {
    position: relative;
    width: 1200px;
    height: 428px;
    overflow: hidden;
    background: linear-gradient(180deg, var(--bg-top), var(--bg-bottom));
    font-family: "Open Sans", Arial, sans-serif;
  }
  .card {
    position: absolute;
    top: 62px;
    height: 301px;
    background: var(--card);
    border-radius: 26px;
    overflow: hidden;
    box-shadow: 0 1px 3px rgba(0,0,0,0.12);
  }
  .card-front { left: 51px; width: 543px; }
  .card-back { left: 606px; width: 542px; }
  .card p, .card h1, .card h2 { margin: 0; line-height: 1; white-space: nowrap; }

  .front-band { position: absolute; left: 0; top: 0; width: 543px; height: 140px; }
  .brand-name {
    position: absolute; left: 48px; top: 34px;
    font-size: 52px; font-weight: 700; color: #fff; letter-spacing: -0.5px;
  }
  .slogan {
    position: absolute; left: 48px; top: 91px;
    font-size: 17px; font-weight: 700; color: #fff;
  }
  .slogan em { font-style: normal; color: var(--yellow); }

  .person-name {
    position: absolute; left: 48px; top: 141px;
    font-size: 20px; font-weight: 700; color: var(--blue);
  }
  .person-role {
    position: absolute; left: 48px; top: 168px;
    font-size: 17px; color: var(--ink);
  }
  .contacts {
    position: absolute; left: 48px; top: 198px; margin: 0; padding: 0; list-style: none;
    font-size: 14px; color: var(--ink);
  }
  .contacts li { display: flex; align-items: center; height: 21.5px; }
  .contacts svg { width: 15px; height: 15px; margin-right: 14px; flex: none; }

  .offer-title {
    position: absolute; right: 32px; top: 40px;
    font-size: 43px; font-weight: 600; color: var(--blue);
  }
  .promo-label {
    position: absolute; right: 32px; top: 100px;
    font-size: 33px; font-weight: 300; color: var(--yellow);
  }
  .promo-code {
    position: absolute; right: 32px; top: 132px;
    font-size: 22px; color: var(--blue);
  }
  .card .promo-note {
    position: absolute; right: 32px; top: 206px;
    text-align: right; font-size: 15px; line-height: 22.5px; color: var(--ink);
  }

  .brand-feature {
    position: absolute; left: 408px; top: 236px; margin: 0;
    font-size: 100px; font-weight: 700; color: var(--blue); line-height: 1; letter-spacing: 2px;
  }
</style>
</head>
<body>
<main class="canvas">
  <section class="card card-front">
    <svg class="front-band" viewBox="0 0 543 140" aria-hidden="true">
      <defs>
        <linearGradient id="bandFill" x1="0" y1="0" x2="0" y2="1">
          <stop offset="0" stop-color="#0d96d6"/>
          <stop offset="1" stop-color="#2fb3ea"/>
        </linearGradient>
      </defs>
      <path d="M0 0 H543 V112 C470 126 390 108 300 116 C200 126 100 138 0 128 Z" fill="url(#bandFill)"/>
      <path d="M0 110 C110 124 210 108 320 100 C420 93 490 104 543 96" fill="none" stroke="rgba(255,255,255,0.25)" stroke-width="2"/>
    </svg>
    <h1 class="brand-name">KiraTel</h1>
    <p class="slogan">Your <em>Family Safety</em> Service</p>

    <h2 class="person-name">Daniel Okafor</h2>
    <p class="person-role">Co-founder</p>
    <ul class="contacts">
      <li>
        <svg viewBox="0 0 16 16" aria-label="Mobile"><rect x="4.5" y="1" width="7" height="14" rx="1.5" fill="var(--blue)"/><rect x="6" y="3" width="4" height="7" fill="#fff"/></svg>
        +55 (11) 5080 6172
      </li>
      <li>
        <svg viewBox="0 0 16 16" aria-label="Phone"><path d="M1 6 C3 2 13 2 15 6 L12 7 L11 5 H5 L4 7 Z" fill="var(--blue)"/><rect x="3" y="8" width="10" height="6" rx="1" fill="var(--blue)"/></svg>
        +55 (11) 9087 614352
      </li>
      <li>
        <svg viewBox="0 0 16 16" aria-label="Email"><text x="8" y="13" text-anchor="middle" font-size="15" font-weight="700" fill="var(--blue)" font-family="Arial, sans-serif">@</text></svg>
        name@kiratel-example.com
      </li>
      <li>
        <svg viewBox="0 0 16 16" aria-label="Website"><circle cx="8" cy="8" r="6.5" fill="none" stroke="var(--blue)" stroke-width="1.5"/><ellipse cx="8" cy="8" rx="3" ry="6.5" fill="none" stroke="var(--blue)" stroke-width="1.2"/><line x1="1.5" y1="8" x2="14.5" y2="8" stroke="var(--blue)" stroke-width="1.2"/></svg>
        www.kiratel-example.com
      </li>
    </ul>
  </section>

  <section class="card card-back">
    <h2 class="offer-title">Try KiraTel free Today!</h2>
    <p class="promo-label">Your personal promo code:</p>
    <p class="promo-code">xxxx-2222-uuuu-7777-1234</p>
    <p class="promo-note">Promo code text explanation<br>with the instructions about<br>the trial offer</p>
  </section>

  <p class="brand-feature">KiraTel</p>
</main>
</body>
</html>
```